Plumbing website that stands out

Seo optimized, mobile friendly, easily editable word press Plumbing website with google reviews widget. And widget of revolving photos of completed work. Contact page and services page, about page. Will provide, “About” content. And photos Need all other content written.
Services include:
Water heater replacement
Tankless water heater installation
Kitchen and bath remodel
Drain cleaning and clog removal
Leak repair
Faucet repair and replacement

I will be adding services and photos of recent completed projects as time goes on.

```html
<!DOCTYPE html>
<html lang="en">
<head>
<meta charset="utf-8">
<title>Clearline Plumbing</title>
<link href="https://fonts.googleapis.com/css2?family=Poppins:wght@400;500;600;700&display=swap" rel="stylesheet">
<style>
:root{
  --sky:#5bb8d0;
  --navy:#2a5ea8;
  --ink:#2a3340;
  --muted:#707a86;
  --slate:#47505b;
  --band:#f5f6f8;
  --white:#ffffff;
}
*{box-sizing:border-box;margin:0;padding:0}
html,body{width:1200px;height:5391px;overflow:hidden}
body{font-family:"Poppins",sans-serif;color:var(--ink);background:var(--white);position:relative;font-size:12px}
.abs{position:absolute}
.ph{border-radius:0}
.btn{display:inline-block;background:var(--sky);color:#fff;font-weight:600;font-size:11px;padding:0 26px;height:40px;line-height:40px;border-radius:2px}
.eyebrow{color:var(--sky);font-size:12px;font-weight:500}
.h2{color:var(--navy);font-size:24px;font-weight:600;line-height:1.25}
.p{color:var(--muted);font-size:11px;line-height:1.7}

/* top bar */
.topbar{left:0;top:0;width:1200px;height:36px;background:var(--sky);color:#fff;font-size:10px}
.topbar .hours{left:163px;top:11px}
.topbar .soc{top:9px;width:18px;height:18px;border-radius:50%;background:var(--navy)}
/* header */
.brand{left:163px;top:66px;display:flex;align-items:center;gap:10px}
.brand .mark{width:30px;height:30px;background:var(--navy)}
.brand .name{color:var(--navy);font-size:17px;font-weight:600;letter-spacing:1px}
.info{top:62px;display:flex;gap:12px;align-items:flex-start}
.info .ic{width:36px;height:36px;border-radius:50%;background:var(--navy);display:flex;align-items:center;justify-content:center}
.info b{display:block;font-size:12px;font-weight:500;color:var(--ink);margin-bottom:3px}
.info span{font-size:10px;color:var(--muted);line-height:1.6}
.nav{left:163px;top:151px;width:874px;height:58px;background:var(--navy);z-index:3;display:flex;align-items:center;font-size:12px;font-weight:500;color:#fff;letter-spacing:.5px}
.nav a{padding:0 37px}
.nav a.on{color:var(--sky)}
.nav .book{margin-left:auto;background:var(--sky);height:58px;line-height:58px;width:127px;text-align:center;padding:0}
/* hero */
.hero{left:0;top:178px;width:1200px;height:700px;background:linear-gradient(100deg,#b9a58c 0%,#d7cdbf 40%,#c7b49d 70%,#8f7a63 100%)}
.hero h1{left:163px;top:358px;width:430px;color:#fff;font-size:44px;font-weight:700;line-height:1.2}
.hero-copy{left:163px;top:527px;width:400px;color:#fff;font-size:11px;line-height:1.6}
.play{left:808px;top:540px;width:54px;height:54px;border-radius:50%;background:#fff;display:flex;align-items:center;justify-content:center}

/* about */
.about-img{background:linear-gradient(135deg,#d9d2c8,#8e8070)}
.about .feat{top:1200px;width:200px}
.about .feat h4{color:var(--muted);font-size:16px;font-weight:500;margin:10px 0 10px}

/* services */
.services{left:0;top:1491px;width:1200px;height:1106px;background:var(--band)}
.card-img{width:276px;height:276px;background:linear-gradient(160deg,#e3e4e6,#9aa3ad)}
.card{width:248px;height:236px;background:#fff;text-align:center;padding:26px 18px 0}
.card h3{color:var(--navy);font-size:14px;font-weight:500;line-height:1.35;margin:12px 0 10px}
.card .more{font-size:10px;font-weight:500;color:var(--ink);margin-top:14px}

/* process */
.step{width:270px;text-align:center}
.step .bubble{width:74px;height:74px;margin:0 auto;border-radius:50% 50% 50% 0;transform:rotate(-45deg);background:var(--navy);border:6px solid #dbe6f3;display:flex;align-items:center;justify-content:center}
.step .bubble svg{transform:rotate(45deg)}
.step h4{color:var(--navy);font-size:14px;font-weight:500;margin:24px 0 12px}

/* why */
.why-img{left:0;top:3072px;width:600px;height:488px;background:linear-gradient(120deg,#6c6e72,#a9aaa8 50%,#3b3e43)}
.why{left:600px;top:3072px;width:600px;height:488px;background:var(--slate);color:#fff}
.why .list{display:grid;grid-template-columns:230px 200px;row-gap:22px;font-size:11px}
.why .list div{display:flex;align-items:center;gap:12px}

/* portfolio */
.work{top:3795px;width:231px;height:343px;background:linear-gradient(160deg,#b8bec6,#5b6a7b)}

/* appointment */
.appt{left:0;top:4220px;width:1200px;height:712px;background:linear-gradient(180deg,#263140,#2f3b4a)}
.form-card{left:163px;top:4471px;width:874px;height:461px;background:#fff;box-shadow:0 4px 20px rgba(0,0,0,.08)}
.field label{display:block;font-size:11px;color:var(--ink);margin-bottom:8px}
.field .in{height:30px;border:1px solid #e2e5e9;font-size:10px;color:#a0a7b0;padding:8px 12px}

/* footer */
.footer{left:0;top:4932px;width:1200px;height:459px;background:var(--navy);color:#fff}
.footer h5{font-size:12px;font-weight:500;padding-bottom:14px;border-bottom:1px solid rgba(255,255,255,.35);width:190px;margin-bottom:18px}
.footer li{list-style:none;font-size:11px;margin-bottom:14px;display:flex;align-items:center;gap:10px}
</style>
</head>
<body>

<!-- top bar -->
<div class="abs topbar">
  <div class="abs hours">&#9679;&nbsp; Mon-Sun : 9.00 AM - 5.00 PM</div>
  <div class="abs soc" style="left:946px"></div>
  <div class="abs soc" style="left:982px"></div>
  <div class="abs soc" style="left:1016px"></div>
</div>

<!-- header -->
<div class="abs brand"><div class="mark"></div><div class="name">CLEARLINE PLUMBING</div></div>
<div class="abs info" style="left:488px">
  <div class="ic"><svg width="16" height="16" viewBox="0 0 24 24" fill="none" stroke="#fff" stroke-width="2"><path d="M12 22s7-7 7-12a7 7 0 0 0-14 0c0 5 7 12 7 12z"/><circle cx="12" cy="10" r="2.5"/></svg></div>
  <div><b>Office Address</b><span>#48 Harbor Lane,<br>Easton , USA</span></div>
</div>
<div class="abs info" style="left:680px">
  <div class="ic"><svg width="16" height="16" viewBox="0 0 24 24" fill="none" stroke="#fff" stroke-width="2"><path d="M5 3h4l2 5-3 2a12 12 0 0 0 6 6l2-3 5 2v4a2 2 0 0 1-2 2A17 17 0 0 1 3 5a2 2 0 0 1 2-2z"/></svg></div>
  <div><b>Call Us</b><span>+1 (555) 014 2290</span></div>
</div>
<div class="abs info" style="left:858px">
  <div class="ic"><svg width="16" height="16" viewBox="0 0 24 24" fill="none" stroke="#fff" stroke-width="2"><rect x="3" y="5" width="18" height="14"/><path d="M3 6l9 7 9-7"/></svg></div>
  <div><b>Send Your Mail</b><span>hello@clearlineplumbing.com</span></div>
</div>

<nav class="abs nav">
  <a class="on">HOME</a><a>ABOUT US</a><a>OUR SERVICES</a><a>FAQ</a><a>CONTACT US</a><a class="book">Book Now</a>
</nav>

<!-- hero -->
<div class="abs hero" role="img" aria-label="Smiling plumber in overalls fixing a sink pipe with a wrench"></div>
<svg class="abs" style="left:0;top:640px" width="1200" height="240" viewBox="0 0 1200 240" aria-hidden="true">
  <path d="M0 110 C300 200 700 220 1200 60 L1200 240 L0 240 Z" fill="#fff"/>
  <path d="M0 100 C300 190 700 210 1200 50 L1200 70 C700 228 300 212 0 130 Z" fill="var(--navy)"/>
  <path d="M0 50 C260 150 560 170 900 130 C600 190 300 180 0 100 Z" fill="var(--sky)"/>
</svg>
<h1 class="abs hero h1" style="position:absolute;left:163px;top:358px;width:430px;height:auto;background:none;color:#fff;font-size:44px;font-weight:700;line-height:1.2">Best Plumbing Services That You Can Trust</h1>
<p class="abs hero-copy">Lorem ipsum dolor sit amet, consectetur adipiscing elit, sed do eiusmod tempor incididunt ut labore et dolore magna aliqua. Ut enim ad minim veniam, quis nostrud exercitation ullamco</p>
<div class="abs btn" style="left:163px;top:603px">&raquo; Contact Us Now</div>
<div class="abs play"><svg width="16" height="16" viewBox="0 0 16 16"><path d="M5 3l8 5-8 5z" fill="#222"/></svg></div>

<!-- about -->
<div class="about">
  <div class="abs about-img" style="left:252px;top:996px;width:340px;height:408px" role="img" aria-label="Plumber with clipboard in a kitchen"></div>
  <div class="abs about-img" style="left:163px;top:1246px;width:235px;height:158px;border:6px solid #fff;box-sizing:content-box;margin:-6px" role="img" aria-label="Plumber working under a sink"></div>
  <div class="abs eyebrow" style="left:647px;top:1010px">About Us</div>
  <div class="abs h2" style="left:647px;top:1040px;width:340px">Professional Plumbing Services Provider</div>
  <p class="abs p" style="left:647px;top:1116px;width:360px">Lorem ipsum dolor sit amet, consectetur adipiscing elit, sed do eiusmod tempor incididunt ut labore et dolore magna aliqua Ut enim ad minim veniam</p>
  <div class="abs feat" style="left:647px">
    <svg width="34" height="34" viewBox="0 0 34 34" fill="none" stroke="var(--sky)" stroke-width="1.6"><circle cx="17" cy="17" r="11"/><circle cx="17" cy="17" r="5"/><path d="M17 2v8M17 24v8M2 17h8M24 17h8"/></svg>
    <h4>Our Vision</h4>
    <p class="p">Lorem ipsum dolor sit amet, consecte adipiscing elit, sed do eiusmod tempor incididunt</p>
  </div>
  <div class="abs feat" style="left:857px">
    <svg width="34" height="34" viewBox="0 0 34 34" fill="none" stroke="var(--sky)" stroke-width="1.6"><path d="M8 26c2-10 8-18 20-20-2 12-10 18-20 20z"/><circle cx="20" cy="14" r="3"/><path d="M5 29l5-5"/></svg>
    <h4>Our Mission</h4>
    <p class="p">Lorem ipsum dolor sit amet, consecte adipiscing elit, sed do eiusmod tempor incididunt</p>
  </div>
  <div class="abs btn" style="left:647px;top:1362px">&raquo; Explore More</div>
</div>

<!-- services -->
<div class="abs services"></div>
<div class="abs eyebrow" style="left:163px;top:1515px">Our Services</div>
<div class="abs h2" style="left:163px;top:1545px;width:310px">The Perfect Solution For All Plumbing Service</div>
<p class="abs p" style="left:504px;top:1566px;width:370px">Lorem ipsum dolor sit amet, consectetur adipiscing elit, sed do eiusmod tempor incididunt ut labore et dolore magna aliqua</p>
<div class="abs btn" style="left:905px;top:1566px;height:38px;line-height:38px;padding:0 24px">&raquo; All Services</div>

<!-- row 1 -->
<div class="abs card-img" style="left:163px;top:1656px" role="img" aria-label="Plumber beside a wall-mounted water heater"></div>
<div class="abs card-img" style="left:463px;top:1638px" role="img" aria-label="Plumber in hard hat installing a tankless heater"></div>
<div class="abs card-img" style="left:762px;top:1656px" role="img" aria-label="Plumber fitting a kitchen appliance"></div>
<div class="abs card-img" style="left:163px;top:2107px" role="img" aria-label="Plumber repairing a leak under a cabinet"></div>
<div class="abs card-img" style="left:463px;top:2089px" role="img" aria-label="Hand with wrench tightening a faucet"></div>
<div class="abs card-img" style="left:762px;top:2089px" role="img" aria-label="Gloved hand clearing a sink drain"></div>

<div class="abs card" style="left:177px;top:1840px"><svg width="30" height="30" viewBox="0 0 30 30" fill="none" stroke="#9aa3ad" stroke-width="1.5"><rect x="8" y="4" width="14" height="20" rx="2"/><path d="M11 24v3M19 24v3M11 10h8"/></svg><h3>Water Heater Replacement</h3><p class="p">Lorem ipsum dolor sit amet, consectet adipiscing elit, sed do eiusmod tempor incididunt</p><div class="more">Read More &rarr;</div></div>
<div class="abs card" style="left:477px;top:1822px"><svg width="30" height="30" viewBox="0 0 30 30" fill="none" stroke="#9aa3ad" stroke-width="1.5"><rect x="8" y="4" width="14" height="16" rx="2"/><path d="M12 20v6M18 20v6M12 9h6M12 13h6"/></svg><h3>Tankless Water Heater Installation</h3><p class="p">Lorem ipsum dolor sit amet, consectet adipiscing elit, sed do eiusmod tempor incididunt</p><div class="more">Read More &rarr;</div></div>
<div class="abs card" style="left:776px;top:1840px"><svg width="30" height="30" viewBox="0 0 30 30" fill="none" stroke="#9aa3ad" stroke-width="1.5"><path d="M4 26h22M6 26V14h18v12M10 14V6h4v8M18 10h4"/></svg><h3>Kitchen And Bath Remodel</h3><p class="p">Lorem ipsum dolor sit amet, consectet adipiscing elit, sed do eiusmod tempor incididunt</p><div class="more">Read More &rarr;</div></div>

<div class="abs card" style="left:177px;top:2291px"><svg width="30" height="30" viewBox="0 0 30 30" fill="none" stroke="#9aa3ad" stroke-width="1.5"><path d="M6 6h18v6H6zM13 12v8M17 12v8"/><path d="M15 22c-2 3 2 3 0 6"/></svg><h3>Leak Repair</h3><p class="p">Lorem ipsum dolor sit amet, consectet adipiscing elit, sed do eiusmod tempor incididunt</p><div class="more">Read More &rarr;</div></div>
<div class="abs card" style="left:477px;top:2273px"><svg width="30" height="30" viewBox="0 0 30 30" fill="none" stroke="#9aa3ad" stroke-width="1.5"><path d="M8 8h14M15 8v6M8 14h14v6H8zM18 20v6"/></svg><h3>Faucet Repair And Replacement</h3><p class="p">Lorem ipsum dolor sit amet, consectet adipiscing elit, sed do eiusmod tempor incididunt</p><div class="more">Read More &rarr;</div></div>
<div class="abs card" style="left:776px;top:2273px"><svg width="30" height="30" viewBox="0 0 30 30" fill="none" stroke="#9aa3ad" stroke-width="1.5"><path d="M6 6l8 8M14 14l4 4 6-2-2 6-6 2z"/><circle cx="9" cy="20" r="2"/></svg><h3>Drain Cleaning And Clog Removal</h3><p class="p">Lorem ipsum dolor sit amet, consectet adipiscing elit, sed do eiusmod tempor incididunt</p><div class="more">Read More &rarr;</div></div>

<!-- process -->
<div class="abs eyebrow" style="left:0;width:1200px;text-align:center;top:2615px">Process</div>
<div class="abs h2" style="left:0;width:1200px;text-align:center;top:2645px">How Do We work?</div>
<svg class="abs" style="left:360px;top:2756px" width="480" height="4" aria-hidden="true"><line x1="0" y1="2" x2="480" y2="2" stroke="#c5ccd6" stroke-dasharray="4 4"/></svg>
<div class="abs step" style="left:185px;top:2722px">
  <div class="bubble"><svg width="28" height="28" viewBox="0 0 28 28" fill="none" stroke="#fff" stroke-width="1.6"><rect x="4" y="6" width="20" height="18"/><path d="M4 11h20M9 3v5M19 3v5M8 15h3M13 15h3M18 15h3M8 19h3M13 19h3"/></svg></div>
  <h4>Make Appointment</h4><p class="p">Lorem ipsum dolor sit amet, consecte adipiscing elit, sed do eiusmod tempor incididunt ut labore et dolore</p>
</div>
<div class="abs step" style="left:464px;top:2722px">
  <div class="bubble"><svg width="28" height="28" viewBox="0 0 28 28" fill="none" stroke="#fff" stroke-width="1.6"><rect x="5" y="4" width="18" height="20"/><path d="M9 10h10M9 14h10M9 18h6"/></svg></div>
  <h4>Give Your Detail</h4><p class="p">Lorem ipsum dolor sit amet, consecte adipiscing elit, sed do eiusmod tempor incididunt ut labore et dolore</p>
</div>
<div class="abs step" style="left:742px;top:2722px">
  <div class="bubble"><svg width="28" height="28" viewBox="0 0 28 28" fill="none" stroke="#fff" stroke-width="1.6"><path d="M7 12a7 7 0 0 1 14 0zM6 12h16"/><path d="M9 14a5 5 0 0 0 10 0M6 26c1-5 4-6 8-6s7 1 8 6"/></svg></div>
  <h4>We Solve Your Problem</h4><p class="p">Lorem ipsum dolor sit amet, consecte adipiscing elit, sed do eiusmod tempor incididunt ut labore et dolore</p>
</div>
<div class="abs btn" style="left:514px;top:2962px;width:172px;text-align:center;padding:0">&raquo; Contact Us Now</div>

<!-- why choose -->
<div class="abs why-img" role="img" aria-label="Plumber fitting a kitchen faucet beside a bowl of fruit"></div>
<div class="abs why">
  <div class="abs eyebrow" style="left:90px;top:94px">Why Choose Us</div>
  <div class="abs" style="left:90px;top:122px;width:380px;font-size:24px;font-weight:600;line-height:1.25">The Perfect Solution For All Plumbing Service</div>
  <p class="abs" style="left:90px;top:196px;width:410px;font-size:11px;line-height:1.7;color:#e3e6ea">Lorem ipsum dolor sit amet, consectetur adipiscing elit, sed do eiusmod tempor incididunt ut labore et dolore magna aliqua. Ut enim ad minim veniam, quis nostrud xercitation ullamco laboris nisi ut aliquip ex ea commodo</p>
  <div class="abs list" style="left:90px;top:296px">
    <div><svg width="24" height="24" viewBox="0 0 24 24" fill="none" stroke="var(--sky)" stroke-width="1.5"><path d="M3 20h18M5 20v-6h3v6M10 20v-9h3v9M15 20V8h3v12"/></svg>Affordable Pricing</div>
    <div><svg width="24" height="24" viewBox="0 0 24 24" fill="none" stroke="var(--sky)" stroke-width="1.5"><path d="M4 4h6v6H4zM14 14h6v6h-6zM10 7h4v10"/></svg>235+ Projects Done</div>
    <div><svg width="24" height="24" viewBox="0 0 24 24" fill="none" stroke="var(--sky)" stroke-width="1.5"><rect x="4" y="4" width="16" height="16"/><path d="M8 9h8M8 13h8M8 17h4"/></svg>Plumbing Experts</div>
    <div><svg width="24" height="24" viewBox="0 0 24 24" fill="none" stroke="var(--sky)" stroke-width="1.5"><circle cx="12" cy="10" r="5"/><path d="M10 16h4v4h-4zM12 2v2M4 10H2M22 10h-2"/></svg>Modern Technology</div>
    <div><svg width="24" height="24" viewBox="0 0 24 24" fill="none" stroke="var(--sky)" stroke-width="1.5"><path d="M4 4l16 16M20 4L4 20M4 4h4M20 4v4"/></svg>Fast Service</div>
    <div><svg width="24" height="24" viewBox="0 0 24 24" fill="none" stroke="var(--sky)" stroke-width="1.5"><circle cx="12" cy="12" r="8"/><path d="M12 7v5l3 2"/></svg>24/7 Services</div>
  </div>
</div>

<!-- portfolio -->
<div class="abs eyebrow" style="left:0;width:1200px;text-align:center;top:3648px">Our Portfolio</div>
<div class="abs h2" style="left:0;width:1200px;text-align:center;top:3678px;color:var(--ink)">Our Latest Projects</div>
<p class="abs p" style="left:390px;top:3724px;width:420px;text-align:center">Lorem ipsum dolor sit amet, consectetur adipiscing elit, sed do eiusmod tempor incididunt ut labore et dolore magna aliqua</p>
<div class="abs work" style="left:31px" role="img" aria-label="Plumber lying under a kitchen cabinet"></div>
<div class="abs work" style="left:323px" role="img" aria-label="Plumber kneeling at a bathroom pipe"></div>
<div class="abs work" style="left:615px" role="img" aria-label="Plumber with a red bucket under a sink"></div>
<div class="abs work" style="left:907px" role="img" aria-label="Plumber servicing a water heater"></div>

<!-- appointment -->
<div class="abs appt"></div>
<div class="abs eyebrow" style="left:0;width:1200px;text-align:center;top:4306px">Make Appointment</div>
<div class="abs" style="left:0;width:1200px;text-align:center;top:4337px;color:#fff;font-size:24px;font-weight:600">Book An Appointment Now</div>
<p class="abs" style="left:380px;top:4384px;width:440px;text-align:center;color:#e3e6ea;font-size:11px;line-height:1.7">Lorem ipsum dolor sit amet, consectetur adipiscing elit, sed do eiusm tempor incididunt ut labore et dolore magna aliqua</p>
<div class="abs form-card">
  <div class="abs" style="left:0;top:0;width:376px;height:461px;background:linear-gradient(160deg,#e7e6e2,#b3b7bd 60%,#4a5a78)" role="img" aria-label="Cheerful plumber giving a thumbs up beside a sink"></div>
  <div class="abs field" style="left:414px;top:44px;width:206px"><label>Name</label><div class="in">Name</div></div>
  <div class="abs field" style="left:628px;top:44px;width:208px"><label>Email</label><div class="in">Email</div></div>
  <div class="abs field" style="left:414px;top:116px;width:206px"><label>Phone</label><div class="in">Phone</div></div>
  <div class="abs field" style="left:628px;top:116px;width:208px"><label>Select Service</label><div class="in" style="color:var(--ink);display:flex;justify-content:space-between">Water Heater Replacement<span>&#9662;</span></div></div>
  <div class="abs field" style="left:414px;top:188px;width:206px"><label>Date</label><div class="in">Date</div></div>
  <div class="abs field" style="left:628px;top:188px;width:208px"><label>Time</label><div class="in">Time</div></div>
  <div class="abs field" style="left:414px;top:260px;width:422px"><label>Message</label><div class="in" style="height:88px">Message</div></div>
  <div class="abs btn" style="left:414px;top:371px;width:422px;text-align:center;padding:0">&raquo; Send Your Request</div>
</div>

<!-- footer -->
<footer class="abs footer">
  <div class="abs" style="left:163px;top:120px;display:flex;align-items:center;gap:10px"><div style="width:30px;height:30px;background:#fff"></div><div style="font-size:18px;font-weight:600;letter-spacing:1px">CLEARLINE PLUMBING</div></div>
  <p class="abs" style="left:163px;top:206px;width:290px;font-size:11px;line-height:1.7;color:#e6ecf6">Lorem ipsum dolor sit amet, consectet adipiscing elit, sed do eiusmod tempor incididunt ut labore et dolore</p>
  <div class="abs" style="left:163px;top:290px;display:flex;gap:16px">
    <div style="width:30px;height:30px;border-radius:50%;background:var(--sky)"></div>
    <div style="width:30px;height:30px;border-radius:50%;background:var(--sky)"></div>
    <div style="width:30px;height:30px;border-radius:50%;background:var(--sky)"></div>
  </div>
  <div class="abs" style="left:607px;top:72px">
    <h5>Quick Links</h5>
    <ul><li>About Us</li><li>Services</li><li>Portfolio</li><li>Contact</li></ul>
  </div>
  <div class="abs" style="left:819px;top:72px">
    <h5>Get In Touch</h5>
    <ul>
      <li><svg width="12" height="12" viewBox="0 0 24 24" fill="none" stroke="var(--sky)" stroke-width="2.4"><path d="M12 22s7-7 7-12a7 7 0 0 0-14 0c0 5 7 12 7 12z"/></svg>#48 Harbor Lane, Easton, USA</li>
      <li><svg width="12" height="12" viewBox="0 0 24 24" fill="none" stroke="var(--sky)" stroke-width="2.4"><rect x="3" y="5" width="18" height="14"/><path d="M3 6l9 7 9-7"/></svg>hello@clearlineplumbing.com</li>
      <li><svg width="12" height="12" viewBox="0 0 24 24" fill="none" stroke="var(--sky)" stroke-width="2.4"><path d="M5 3h4l2 5-3 2a12 12 0 0 0 6 6l2-3 5 2v4a2 2 0 0 1-2 2A17 17 0 0 1 3 5a2 2 0 0 1 2-2z"/></svg>+1 (555) 014 2290</li>
    </ul>
  </div>
  <div class="abs" style="left:0;top:373px;width:1200px;text-align:center;font-size:10px">Copyright &copy; 2023 Clearline Plumbing | Powered by Clearline Plumbing</div>
</footer>

</body>
</html>
```